Real Estate Agent needs business card design

We have logo designed already, want to have business card designed. Very interested in those smaller size business card as they look very trendy. Business name is called VORENDA REALTY

```html
<!DOCTYPE html>
<html lang="en">
<head>
<meta charset="utf-8">
<title>Vorenda Realty – Business Card</title>
<link href="https://fonts.googleapis.com/css2?family=Open+Sans:wght@400;600;700&display=swap" rel="stylesheet">
<style>
  :root {
    --backdrop: #161616;
    --gold: #c9a46e;
    --gold-deep: #b8894f;
    --paper: #ffffff;
    --ink: #3a3a3a;
    --ink-soft: #2f2f2f;
    --rule: #2b2b2b;
    --on-gold: #ffffff;
  }
  * { box-sizing: border-box; margin: 0; padding: 0; }
  html, body {
    width: 1200px;
    height: 904px;
    overflow: hidden;
    background: var(--backdrop);
    font-family: "Open Sans", Arial, sans-serif;
  }
  .canvas {
    width: 1200px;
    height: 904px;
    display: flex;
    flex-direction: column;
    align-items: center;
    justify-content: center;
    gap: 60px;
  }
  .card {
    width: 720px;
    height: 360px;
    box-shadow: 0 14px 30px rgba(0,0,0,0.55);
  }
  .card--front {
    background: var(--gold);
    display: flex;
    align-items: center;
    justify-content: center;
  }
  .wordmark {
    font-family: "Open Sans", Arial, sans-serif;
    font-weight: 600;
    letter-spacing: 0.12em;
    text-transform: uppercase;
  }
  .card--front .wordmark {
    color: var(--on-gold);
    font-size: 34px;
  }
  .card--back {
    background: var(--paper);
    display: grid;
    grid-template-columns: 408px 1px 1fr;
    align-items: center;
  }
  .card--back .wordmark {
    color: var(--ink);
    font-size: 30px;
    text-align: center;
    padding-left: 40px;
  }
  .divider {
    width: 1px;
    height: 150px;
    background: var(--rule);
  }
  .contact {
    padding-left: 44px;
    color: var(--ink-soft);
    font-size: 15.5px;
    line-height: 1.45;
  }
  .contact__name {
    color: var(--gold-deep);
    font-weight: 700;
    font-size: 19px;
    line-height: 1.3;
  }
  .contact__title { margin-bottom: 14px; }
  .contact__address { margin-bottom: 14px; padding-left: 32px; }
  .contact__line {
    display: flex;
    align-items: center;
    gap: 12px;
    padding-left: 12px;
  }
  .contact__icon { width: 14px; height: 14px; flex: none; }
</style>
</head>
<body>
<main class="canvas">
  <section class="card card--front">
    <span class="wordmark">Vorenda Realty</span>
  </section>

  <section class="card card--back">
    <span class="wordmark">Vorenda Realty</span>
    <span class="divider"></span>
    <div class="contact">
      <p class="contact__name">Helena Marsh</p>
      <p class="contact__title">Senior Property Consultant</p>
      <p class="contact__address">4C, 118 Harbour Street<br>Kirribilli, NSW 2061</p>
      <p class="contact__line">
        <svg class="contact__icon" viewBox="0 0 24 24" aria-hidden="true">
          <path fill="#c9a46e" d="M6.6 10.8a15.1 15.1 0 0 0 6.6 6.6l2.2-2.2a1 1 0 0 1 1-.25 11.4 11.4 0 0 0 3.6.57 1 1 0 0 1 1 1V20a1 1 0 0 1-1 1A17 17 0 0 1 3 4a1 1 0 0 1 1-1h3.5a1 1 0 0 1 1 1c0 1.25.2 2.45.57 3.57a1 1 0 0 1-.25 1z"/>
        </svg>
        0412 555 019
      </p>
      <p class="contact__line">
        <svg class="contact__icon" viewBox="0 0 24 24" aria-hidden="true">
          <circle cx="12" cy="12" r="10" fill="none" stroke="#c9a46e" stroke-width="2"/>
          <path d="M2 12h20M12 2c3 3.5 3 16.5 0 20M12 2c-3 3.5-3 16.5 0 20" fill="none" stroke="#c9a46e" stroke-width="1.6"/>
        </svg>
        www.vorendarealty.com.au
      </p>
    </div>
  </section>
</main>
</body>
</html>
```